Family owned plumbing contractor needs eye catching business card design

Business cards that are unique, eye catching, and provide customers with general company information, such as name, address, phone number, website, employee name/title, cell phone #, & email address. We are transitioning to a new logo that utilizes a more retro feel, so we are interested in seeing some cool old school designs in the mix. We are liking the dark background on some of the samples on this website. If that is workable with our artwork, we would like to see that incorporated into the design.
Contact Information for Business Card
Copperline Pipeworks, Inc.
www.copperlinepipeworks.example
(555) 630-2918 phone
Nevada License #64205
California License #5870413
Glen Harwick, President
(555) 418-9063 cell
glen@copperlinepipeworks.example
Residential * Commercial * Service
Requirements
Must have
- The business card details listed above & logo provided.
Nice to have
- I made some notes about color options in the description.

```html
<!DOCTYPE html>
<html lang="en">
<head>
<meta charset="utf-8">
<title>Copperline Pipeworks, Inc. — Business Card</title>
<link rel="stylesheet" href="https://fonts.googleapis.com/css2?family=Lato:wght@400;700&display=swap">
<style>
  :root {
    --page: #d9dde1;
    --blue-light: #6a8eaa;
    --blue-dark: #3f6582;
    --teal: #86d9c2;
    --paper: #f4f5f4;
    --ink-light: #eef3f6;
    --shadow: rgba(20, 35, 50, 0.28);
  }
  * { box-sizing: border-box; margin: 0; padding: 0; }
  html, body {
    width: 1200px; height: 900px; overflow: hidden;
    background: var(--page);
    font-family: "Lato", sans-serif;
  }
  .stage {
    position: relative; width: 1200px; height: 900px;
    display: flex; flex-direction: column; align-items: center; justify-content: center; gap: 44px;
  }
  .card {
    position: relative; width: 640px; height: 366px; overflow: hidden;
    box-shadow: 0 12px 30px var(--shadow);
  }
  .card-back {
    background: radial-gradient(ellipse at 55% 35%, var(--blue-light), var(--blue-dark) 90%);
    display: flex; flex-direction: column; align-items: center; justify-content: center;
  }
  .brand-mark {
    display: flex; align-items: center; gap: 14px;
    color: var(--teal); font-weight: 700; font-size: 26px; letter-spacing: .5px;
  }
  .brand-dot {
    width: 22px; height: 22px; border-radius: 50%; background: var(--teal); flex: none;
  }
  .tagline {
    margin-top: 42px; color: var(--ink-light); font-size: 15px; letter-spacing: 1px;
  }
  .card-front { background: linear-gradient(160deg, var(--blue-light), var(--blue-dark)); }
  .card-art { position: absolute; inset: 0; }
  .front-brand {
    position: absolute; left: 20px; top: 160px; width: 300px;
    flex-direction: column; gap: 10px; text-align: center; font-size: 20px;
    color: var(--blue-dark); white-space: nowrap;
  }
  .front-brand .brand-dot { background: var(--blue-dark); }
  .details {
    position: absolute; left: 398px; top: 80px; color: var(--ink-light);
    font-size: 13.5px; line-height: 1.35;
  }
  .person-name { color: var(--teal); font-size: 21px; font-weight: 700; line-height: 1.2; }
  .person-title { margin-bottom: 20px; }
  .licenses { margin-bottom: 16px; }
  .company { color: var(--teal); font-weight: 700; font-size: 14px; margin-bottom: 2px; }
  .contact-list { list-style: none; }
  .contact-list li { display: flex; align-items: center; gap: 6px; white-space: nowrap; }
  .contact-icon { width: 11px; height: 11px; flex: none; }
</style>
</head>
<body>
<main class="stage">
  <section class="card card-back">
    <div class="brand-mark"><span class="brand-dot"></span>Copperline Pipeworks, Inc.</div>
    <p class="tagline">Residential ✱ Commercial ✱ Service</p>
  </section>

  <section class="card card-front">
    <svg class="card-art" viewBox="0 0 640 366" width="640" height="366" aria-hidden="true">
      <path d="M0 0 H352 Q440 220 198 366 H0 Z" fill="var(--teal)"/>
      <path d="M0 0 H338 Q420 215 184 366 H0 Z" fill="#ffffff"/>
      <path d="M0 0 H326 Q406 212 172 366 H0 Z" fill="var(--paper)"/>
    </svg>
    <div class="brand-mark front-brand"><span class="brand-dot"></span>Copperline Pipeworks, Inc.</div>
    <div class="details">
      <p class="person-name">Glen Harwick</p>
      <p class="person-title">President</p>
      <p class="licenses">Nevada License #64205<br>California License #5870413</p>
      <p class="company">Copperline Pipeworks, Inc.</p>
      <ul class="contact-list">
        <li><svg class="contact-icon" viewBox="0 0 12 12"><path d="M2 1h3l1 3-2 1a7 7 0 0 0 3 3l1-2 3 1v3c-6 0-9-3-9-9z" fill="var(--teal)"/></svg>(555) 630-2918</li>
        <li><svg class="contact-icon" viewBox="0 0 12 12"><rect x="3" y="0.5" width="6" height="11" rx="1" fill="none" stroke="var(--teal)"/></svg>(555) 418-9063</li>
        <li><svg class="contact-icon" viewBox="0 0 12 12"><rect x="0.5" y="2.5" width="11" height="7" fill="none" stroke="var(--teal)"/><path d="M.5 2.5 6 7l5.5-4.5" fill="none" stroke="var(--teal)"/></svg>glen@copperlinepipeworks.example</li>
        <li><svg class="contact-icon" viewBox="0 0 12 12"><circle cx="6" cy="6" r="5.5" fill="var(--teal)"/></svg>www.copperlinepipeworks.example</li>
      </ul>
    </div>
  </section>
</main>
</body>
</html>
```